Redesign of a facility management homepage

We need a redesign/an improved design of the facility management homepage (http://www.kolvenhaus-drefling.de/).
This websites offers detailed information on the "About us" as company, the "Services" provided and special information on facility and strata management. We would like to keep the structure of the website.
We need ideas/designs how this website could look more modern and confidential and appealing/pleasant for visitors at the same time and not losing the main purpose of information distribution.
The green color must be used since this is the basic color from our logo.
The blue in the background of the logo ist optional. So feel to use it or not.
We need no coding only design (.psd or as .ai)
Industry/Entity Type
It Company
Look and feel
Each slider illustrates characteristics of the customer's brand and the style your logo design should communicate.

```html
<!DOCTYPE html>
<html lang="de">
<head>
<meta charset="utf-8">
<title>Kolvenhaus Gebäudeservice GmbH Drefling</title>
<link href="https://fonts.googleapis.com/css2?family=Questrial&display=swap" rel="stylesheet">
<style>
:root{
  --green:#078a07;
  --green-light:#0ab30a;
  --green-text:#0a860a;
  --blue:#4079c3;
  --black:#000;
  --white:#fff;
  --border:#c9c9c9;
}
*{margin:0;padding:0;box-sizing:border-box}
html,body{width:1200px;height:1000px;overflow:hidden;background:var(--white);font-family:'Questrial',sans-serif}
.site-header{position:absolute;left:0;top:0;width:1200px;height:163px;background:linear-gradient(#fff 0%,#f6f6f6 40%,#e6e6e6 100%)}
.brand{position:absolute;left:100px;top:42px;width:136px;height:110px;display:flex;align-items:center;gap:8px}
.brand-mark{width:18px;height:18px;background:var(--green)}
.brand-name{color:var(--green-text);font-size:19px}
.tagline{position:absolute;left:260px;top:70px;color:var(--green-text)}
.tagline h1{font-weight:400;font-size:27px;line-height:33px}
.tagline p{font-size:21px;line-height:26px}
.main-nav{position:absolute;left:0;top:163px;width:1200px;height:48px;background:var(--green)}
.main-nav a{position:absolute;top:0;height:48px;line-height:46px;color:var(--white);text-decoration:none;font-size:18px}
.main-nav a.active{background:var(--green-light);width:134px;text-align:center}
.hero{position:absolute;left:101px;top:220px;width:1001px;height:351px}
.contact-panel{position:absolute;left:0;top:0;width:292px;height:305px;background:linear-gradient(160deg,#4a82c9 0%,#3f78c2 55%,#3a70b8 100%);color:var(--white);padding:30px 15px}
.contact-panel h2{font-weight:400;font-size:20px;line-height:21px;margin-bottom:15px}
.contact-panel .legal{font-size:13px;line-height:20px}
.contact-panel .phone{font-size:20px;line-height:25px;margin-top:22px}
.contact-panel .mail{font-size:13px;margin-top:20px;padding-left:2px}
.form-link{position:absolute;left:0;top:305px;width:292px;height:46px;background:var(--black);color:var(--white);font-size:19px;display:flex;align-items:center;padding:0 16px;gap:5px}
.form-link svg.arrow{margin-left:auto}
.slide{position:absolute;left:292px;top:0;width:709px;height:351px;background:
  linear-gradient(180deg,rgba(110,95,60,.85) 0%,rgba(170,150,100,.6) 18%,rgba(240,240,238,.2) 30%,rgba(250,250,250,0) 55%,rgba(60,60,60,.35) 70%,rgba(120,110,100,.7) 100%),
  linear-gradient(90deg,#e4e4e2 0%,#f2f2f0 40%,#dcdcd8 75%,#bdb6a2 100%)}
.slide-caption{position:absolute;right:0;top:271px;height:33px;background:var(--black);color:var(--white);font-size:20px;padding:0 10px;line-height:33px}
.slide-dots{position:absolute;left:881px;top:313px;width:117px;height:32px;background:#111;border-radius:6px;display:flex;align-items:center;justify-content:center;gap:17px}
.slide-dots span{width:12px;height:12px;border-radius:50%;background:var(--white)}
.slide-dots span.on{background:var(--green)}
.tile{position:absolute;top:581px;height:135px;border:1px solid var(--border);background:#fff}
.tile h3{height:51px;background:var(--green);color:var(--white);font-weight:400;font-size:19px;padding:14px 17px 0}
.tile .visual{height:82px}
</style>
</head>
<body>
<header class="site-header">
  <div class="brand"><span class="brand-mark"></span><span class="brand-name">Kolvenhaus</span></div>
  <div class="tagline">
    <h1>Kolvenhaus Gebäudeservice GmbH Drefling</h1>
    <p>Ihr Partner vor Ort.</p>
  </div>
</header>
<nav class="main-nav">
  <a class="active" href="#" style="left:101px">Wir über uns</a>
  <a href="#" style="left:251px">Gebäudemanagement</a>
  <a href="#" style="left:487px">Gebäudeverwaltung</a>
  <a href="#" style="left:690px">Vermietung</a>
</nav>
<section class="hero">
  <div class="contact-panel">
    <h2>Kolvenhaus Gebäudeservice GmbH</h2>
    <p class="legal">Lindenplatz 14 in 04512 Drefling<br>vertreten durch Frau Helga Sommerfeld,<br>Geschäftsführerin<br>AG Drefling, HR.Nr.: HBR 40417</p>
    <p class="phone">Tel.: 034 51 / 72 40 18<br>Fax: 034 51 / 72 40 19</p>
    <p class="mail">Mail: info@kolvenhaus-drefling.de</p>
  </div>
  <a class="form-link">
    <svg width="22" height="15" viewBox="0 0 22 15"><rect x="0.5" y="0.5" width="21" height="14" fill="#fff"/><path d="M1 1 L11 9 L21 1" stroke="#000" stroke-width="1.5" fill="none"/></svg>
    Kontaktformular
    <svg class="arrow" width="10" height="12" viewBox="0 0 10 12"><path d="M0 0 L10 6 L0 12Z" fill="#fff"/></svg>
  </a>
  <div class="slide" role="img" aria-label="Foto: weiße Firmentransporter in einer Reihe auf Kopfsteinpflaster vor Bäumen"></div>
  <div class="slide-caption">Unser Fuhrpark</div>
  <div class="slide-dots"><span class="on"></span><span></span><span></span></div>
</section>
<article class="tile" style="left:100px;width:247px"><h3>Störung online melden</h3><div class="visual" role="img" aria-label="Foto: Servicemitarbeiter mit Headset" style="background:linear-gradient(90deg,#a9c3d8 0%,#d9cbbd 45%,#c89a80 70%,#e9e6e3 100%)"></div></article>
<article class="tile" style="left:352px;width:247px"><h3>Kontakt</h3><div class="visual" role="img" aria-label="Foto: Tastatur mit grüner Kontakt-Taste" style="background:linear-gradient(90deg,#c4c4c4 0%,#a9a9a9 30%,#3aa23a 45%,#2e9a2e 75%,#b9b9b9 85%,#8e8e8e 100%)"></div></article>
<article class="tile" style="left:605px;width:247px"><h3>Links</h3><div class="visual" role="img" aria-label="Foto: Bauplan mit Taschenrechner und Stift" style="background:linear-gradient(90deg,#f4f5f6 0%,#e8ebee 50%,#b9bec3 75%,#e2e5e8 100%)"></div></article>
<article class="tile" style="left:858px;width:245px"><h3>Impressum</h3><div class="visual" role="img" aria-label="Foto: Hände schützen ein kleines Hausmodell" style="background:linear-gradient(90deg,#a9bdd6 0%,#e0a988 30%,#c9cfd8 50%,#d2573e 62%,#e2ae8e 80%,#b5c4d8 100%)"></div></article>
</body>
</html>
```